New Website Design. Porjtect is Guaranteed.

I would like a site similar to this: http://givevehiclehope.org.

old site: http://www.wheelsforbloom.org

Create a professional website; a car donation site seeking leads to return calls.

Please see http://givevehiclehope.org for the concept I am after.

The webpage should have a professional feel. The pages to include are 'Home', 'About us' and 'Get Started'

Industry/Entity Type

It Professional

Coding

Coded - Design and coding required

Number of Pages Required

1 page

```html
<!DOCTYPE html>
<html lang="en">
<head>
<meta charset="utf-8">
<title>Wheels of Hope</title>
<link href="https://fonts.googleapis.com/css2?family=Libre+Baskerville:wght@400;700&family=Open+Sans:wght@400;600&display=swap" rel="stylesheet">
<style>
:root{
  --purple:#5a2d72;
  --purple-soft:#7d619c;
  --purple-line:#9a85b4;
  --yellow:#f1c40f;
  --ink:#333;
  --muted:#777;
  --dark:#3a3a3a;
  --white:#fff;
}
*{margin:0;padding:0;box-sizing:border-box}
html,body{width:791px;height:1200px;overflow:hidden;background:var(--white)}
body{position:relative;font-family:"Open Sans",sans-serif;color:var(--ink)}
.abs{position:absolute}
.serif{font-family:"Libre Baskerville",serif}

/* header */
.site-header{left:0;top:0;width:791px;height:63px;background:var(--purple)}
.brand{left:104px;top:34px;font-size:12px;font-weight:700;color:var(--white)}
.brand-dot{left:104px;top:16px;width:14px;height:14px;border-radius:50%;background:var(--yellow)}
.nav a{position:absolute;top:26px;font-family:"Libre Baskerville",serif;font-size:9.5px;color:var(--white);text-decoration:none;white-space:nowrap}
.nav .active{color:var(--yellow)}
.nav .active::after{content:"";position:absolute;left:-6px;right:-6px;top:34px;height:3px;background:var(--yellow)}
.call{left:468px;top:27px;font-size:8px;color:var(--yellow);white-space:nowrap}
.call b{color:var(--white)}
.btn-yellow{background:var(--yellow);color:var(--white);font-size:8.5px;font-weight:600;display:flex;align-items:center;justify-content:center}
.get-started{left:604px;top:21px;width:84px;height:21px}

/* hero */
.hero{left:0;top:63px;width:791px;height:316px;background:linear-gradient(120deg,#c9c3bd 0%,#ddd6cf 40%,#b7aca3 75%,#8f7e73 100%)}
.hero-title{left:103px;top:160px;font-size:23px;font-weight:700;line-height:31px;color:#111}
.btn-purple{background:var(--purple);color:var(--white);font-size:8.5px;font-weight:600;display:flex;align-items:center;justify-content:center}
.hero-contact{left:102px;top:235px;width:85px;height:21px}

.donate-form{left:505px;top:102px;width:182px;height:216px;background:rgba(255,255,255,.35);border:2px solid rgba(255,255,255,.6)}
.form-banner{left:0;top:0;width:178px}
.form-banner span{position:absolute;left:0;top:8px;width:178px;text-align:center;font-size:11.5px;font-weight:700;color:#222}
.field{position:absolute;height:20px;background:var(--white);font-size:6.5px;color:#777;padding-left:5px;display:flex;align-items:center}
.field.select::after{content:"";position:absolute;right:5px;top:9px;border:3px solid transparent;border-top-color:#555}
.submit{position:absolute;left:13px;top:180px;width:152px;height:19px;background:var(--yellow);font-size:7.5px;color:#222;display:flex;align-items:center;justify-content:center}

/* features */
.features{left:102px;top:364px;width:586px;height:105px;background:var(--purple-soft);display:flex}
.feature{position:relative;flex:1;color:var(--white);font-size:9.5px;text-align:center;display:flex;flex-direction:column;align-items:center;justify-content:center;gap:10px;border-left:1px solid var(--purple-line)}
.feature:first-child{border-left:0}
.feature.highlight{background:var(--yellow);color:#333;margin-top:-6px;height:116px}
.feature-arrow{left:312px;top:464px;width:20px;height:20px}

/* welcome */
.welcome-title{left:0;width:791px;text-align:center;font-size:13px;font-weight:700;color:var(--purple);line-height:16px}
.welcome-title em{font-style:normal;color:var(--yellow)}
.welcome-rule{left:383px;top:559px;width:26px;height:1px;background:var(--purple)}
.welcome-copy{left:190px;top:580px;width:411px;text-align:center;font-size:8.4px;line-height:11.7px;color:var(--muted)}
.discover{left:354px;top:645px;width:84px;height:21px}

/* cards */
.card{top:708px;width:185px;height:190px;border:1px solid #e6e6e6}
.card-media{height:106px}
.card h3{font-weight:400;font-size:10.5px;color:#333;margin:14px 7px 8px}
.card p{font-size:8.4px;line-height:11.7px;color:var(--muted);margin:0 7px}

/* footer */
.footer{left:0;top:940px;width:401px;height:228px;background:var(--purple);color:var(--white)}
.footer-map{left:401px;top:940px;width:390px;height:228px;background:linear-gradient(180deg,#ebebeb,#e2e2e2)}
.f-brand{left:104px;top:985px;font-size:9.5px;font-weight:700;color:var(--white)}
.f-text{left:102px;font-size:8.5px;color:var(--white);white-space:nowrap}
.social{top:1110px;width:22px;height:22px;border-radius:50%;border:1px solid var(--yellow)}
.bottom-bar{left:0;top:1168px;width:791px;height:32px;background:var(--dark);color:var(--white);font-size:8.5px}
</style>
</head>
<body>

<header class="site-header abs">
  <div class="brand abs serif">Wheels of Hope</div>
  <nav class="nav">
    <a class="active" style="left:273px">Home</a>
    <a style="left:322px">About us</a>
    <a style="left:382px">Contact Us</a>
  </nav>
  <div class="call abs serif">Call Us
    <svg width="8" height="10" viewBox="0 0 9 11" style="vertical-align:-2px;margin:0 2px"><path d="M2 0h5v11H2z" fill="none" stroke="#f1c40f" stroke-width="1.4"/><circle cx="4.5" cy="9" r=".8" fill="#f1c40f"/></svg>
    <b>1-888-555-0142</b></div>
  <div class="get-started abs btn-yellow">Get Started</div>
</header>

<section class="hero abs" role="img" aria-label="Cupped hands holding a small red toy car over a striped shirt"></section>
<h1 class="hero-title abs serif">Donate Your Car to<br>Fight Children's Cancer</h1>
<div class="hero-contact abs btn-purple">Contact Us</div>

<form class="donate-form abs">
  <svg class="form-banner abs" width="178" height="44" viewBox="0 0 178 44"><path d="M0 0H178V26L89 44L0 26Z" fill="#f1c40f"/></svg>
  <div class="form-banner abs"><span class="serif">Instantly Donate Online</span></div>
  <div class="field" style="left:13px;top:55px;width:73px">First Name</div>
  <div class="field" style="left:92px;top:55px;width:73px">First Name</div>
  <div class="field" style="left:13px;top:80px;width:152px">Email</div>
  <div class="field" style="left:13px;top:105px;width:73px">Phone</div>
  <div class="field" style="left:92px;top:105px;width:73px">Zip Code</div>
  <div class="field select" style="left:13px;top:130px;width:152px">Year of Vehicle</div>
  <div class="field select" style="left:13px;top:156px;width:73px">Make of Vehicle</div>
  <div class="field select" style="left:92px;top:156px;width:73px">Model of Vehicle</div>
  <div class="submit">Submit Application</div>
</form>

<section class="features abs">
  <div class="feature">
    <svg width="28" height="24" viewBox="0 0 28 24" fill="none" stroke="#fff" stroke-width="1.4"><path d="M2 17h18V11h-6V6H8v5H2z"/><path d="M20 13l5-9M20 7l5-3"/><circle cx="7" cy="19" r="2.5"/><circle cx="17" cy="19" r="2.5"/></svg>
    Towing Is Free</div>
  <div class="feature highlight">
    <svg width="24" height="24" viewBox="0 0 24 24"><circle cx="12" cy="12" r="11" fill="#222"/><path d="M6 7c3 0 4 3 2 5s1 5-1 6M15 3c0 3 3 3 4 6" stroke="#f1c40f" stroke-width="1.5" fill="none"/></svg>
    Donations Accepted<br>Nationwide</div>
  <div class="feature">
    <svg width="34" height="16" viewBox="0 0 34 16" fill="none" stroke="#fff" stroke-width="1.4"><path d="M2 11V8l5-1 4-5h11l5 5 5 1v3z"/><circle cx="9" cy="12" r="2.5"/><circle cx="25" cy="12" r="2.5"/></svg>
    All Vehicle Type &nbsp;Welcome</div>
  <div class="feature">
    <svg width="24" height="26" viewBox="0 0 24 26" fill="none" stroke="#fff" stroke-width="1.4"><path d="M3 1h13v24H3z"/><path d="M6 6h7M6 10h7M6 14h4"/><circle cx="17" cy="19" r="5" fill="#7d619c"/><path d="M15 21l4-4"/></svg>
    Tax Deductible</div>
</section>
<svg class="feature-arrow abs" viewBox="0 0 20 20"><circle cx="10" cy="10" r="9" fill="#f1c40f" stroke="#fff" stroke-width="1.5"/><path d="M6 10h7M10 7l3 3-3 3" stroke="#222" stroke-width="1.6" fill="none"/></svg>

<h2 class="welcome-title abs serif" style="top:524px">Welcome<br>Wheels of <em>Hope</em></h2>
<div class="welcome-rule abs"></div>
<p class="welcome-copy abs">There are many variations of passages of Lorem Ipsum available, but the majority have suffered alteration in some form, by injected humour, or randomised words which don't look even slightly believable. If you are going to use a passage of Lorem Ipsum, you need to be sure there isn't anything embarrassing hidden in the...</p>
<div class="discover abs btn-purple">Discover More</div>

<article class="card abs" style="left:102px">
  <div class="card-media" role="img" aria-label="Hand writing on a tax form beside a calculator" style="background:linear-gradient(135deg,#8a8a8a,#d8d8d8)"></div>
  <h3>Income Tax Deduction</h3>
  <p>We issue you an IRS tax receipt &amp; offer the largest resale network to get you the highest tax write-off possible.</p>
</article>
<article class="card abs" style="left:302px">
  <div class="card-media" role="img" aria-label="Hand signing paperwork next to a calculator" style="background:linear-gradient(135deg,#f2f2f2,#9a9a9a)"></div>
  <h3>No Paperwork Hassles</h3>
  <p>We take any car and handle everything: &nbsp;DMV, Smog, &amp; IRS paperwork.</p>
</article>
<article class="card abs" style="left:503px">
  <div class="card-media" role="img" aria-label="Two men reviewing documents at a car window" style="background:linear-gradient(135deg,#6f7479,#c9c4bd)"></div>
  <h3>Car donations help fund programs</h3>
  <p>And benefit Bright Wish Foundation. An IRS 501(c)3 nonprofit organization.</p>
</article>

<footer>
  <div class="footer abs"></div>
  <div class="footer-map abs" role="img" aria-label="Street map showing the office location"></div>
  <svg class="abs" style="left:588px;top:1027px" width="16" height="22" viewBox="0 0 16 22"><path d="M8 21C3 14 1 11 1 8a7 7 0 0114 0c0 3-2 6-7 13z" fill="#f1c40f"/><circle cx="8" cy="8" r="2.5" fill="#fff"/></svg>
  <div class="brand-dot abs" style="top:981px"></div>
  <div class="f-brand abs serif" style="left:122px">Wheels of Hope</div>
  <div class="f-text abs" style="top:1014px">14 Maple Row, Fairview, 40213, simply random</div>
  <div class="f-text abs" style="top:1039px;font-size:9.5px;font-weight:600">Call Us:</div>
  <div class="f-text abs" style="top:1053px;font-size:13px">1-888-555-0142</div>
  <div class="f-text abs" style="top:1068px">info@wheelsofhope.org</div>
  <div class="f-text abs" style="top:1090px;font-size:9.5px;font-weight:600">Get Social:</div>
  <div class="social abs" style="left:102px"></div>
  <div class="social abs" style="left:129px;background:var(--yellow)"></div>
  <div class="social abs" style="left:156px"></div>
  <div class="bottom-bar abs">
    <span class="abs" style="left:102px;top:10px">© 2017 Bright Wish Foundation. All Rights Reserved.</span>
    <span class="abs" style="left:420px;top:10px;text-decoration:underline">Privacy Policy</span>
    <svg class="abs" style="left:669px;top:6px" width="19" height="19" viewBox="0 0 19 19"><circle cx="9.5" cy="9.5" r="9" fill="#f1c40f"/><path d="M9.5 13V6M6.5 9l3-3 3 3" stroke="#222" stroke-width="1.5" fill="none"/></svg>
  </div>
</footer>

</body>
</html>
```